Company brochure for our unique consulting business

We are a small consulting business offering a unique set of services to our clients.. In simple terms we are a business improvement consultancy helping our clients get the best out of their businesses. We work with clients across multiple sectors and deliver a variety of services. We want to put together a brochure to cover these main themes:1. Who we are2. What we do3. The type of people we employ4. The sectors we work inWhile the brochure needs to have a certain corporate feel to it, we don't want it to be "boring" or "stiff". We would like it to have a slightly "friendly" or "informal" feel to it, to reflect the type of organisation we are.We have a company website http://tollandvergeadvisory.com , however we do not want to directly replicate the content or feel as we recognise it needs updating.We would like the brochure to be A4 portrait format. We anticipate requiring 12 sides (including covers) but we are happy to be guided on this based on the content we have provided.The attached ppt file gives the detail of the content to be included and also shows the proposed pagination. For the front cover we would like to try 2 versions, one with the TVA logo and one with the Tolland Verge Advisory logo (a file of both is attached)One of the most important pages will be the "Our Services" page. We would like this to cover the centre fold. In the ppt file we have shown an example layout, but this is where we need most help - we are clearly not graphic designers! This page will be the most used page in sales meetings etc.Also attached is the following:1. file for our TollandVerge Advisory company logo.2. File for our TVA company logo3. Files for Derek's signatures (for under photos) - Owen's to follow4. Photo of Derek & Owen (person in purple shirt to be cropped out)Thank you and really excited to see what everyone comes back with.Derek & Owen

Target Market(s)

Very broad - Manufacturing, Healthcare, Hospitality

Industry/Entity Type

Management Consulting

Font styles to use
Other font styles liked:
• We use Swiss721, but happy to be guided by designer

Colors
3276b5
85abd2
0355a3
333333
5c5c5c
9d9d9d
d9d9d9

Requirements
Must have
• Corporate feel
Nice to have
• Slightly friendly feel
• Our standard "blue" is (CORRECTION) - R55 G96 B146 #376092 and our standard grey is R197 G178, B179 - #B3B2B2, which we would like to keep, but other colours we are happy to be guided on. Brand guidelines attached.

```html
<!DOCTYPE html>
<html lang="en">
<head>
<meta charset="utf-8">
<title>Tolland Verge Advisory – Brochure</title>
<link href="https://fonts.googleapis.com/css2?family=Arimo:ital,wght@0,400;0,700;1,400&display=swap" rel="stylesheet">
<style>
  :root{
    --brand-blue:#376092;
    --ink:#333333;
    --grey-dark:#5c5c5c;
    --grey-mid:#7d7e82;
    --grey-soft:#9d9d9d;
    --stage:#808080;
    --paper:#ffffff;
  }
  *{box-sizing:border-box;margin:0;padding:0}
  html,body{width:1200px;height:1200px;overflow:hidden}
  body{background:var(--stage);font-family:"Arimo",Arial,sans-serif;position:relative;color:var(--ink)}

  .page{position:absolute;top:338px;width:370px;height:523px;background:var(--paper);overflow:hidden}
  .page--values{left:30px;background:linear-gradient(90deg,#fff 80%,#e2e2e2 100%)}
  .page--welcome{left:400px;background:linear-gradient(90deg,#d6d6d6 0%,#fff 18%)}
  .page--cover{left:800px;background:linear-gradient(100deg,#c9c9c9 0%,#f4f4f4 22%,#fff 45%)}

  /* section headers */
  .section-band{position:absolute;height:26px;background:var(--brand-blue);color:#fff;
    font-weight:700;font-size:14px;line-height:26px;letter-spacing:.5px}
  .stripes{position:absolute;display:flex;gap:4px;height:26px}
  .stripes span{width:4px;background:var(--brand-blue)}

  /* values page */
  .values-band{left:0;top:40px;width:150px;padding-left:22px}
  .values-stripes{left:156px;top:40px}
  .value{position:absolute;left:22px;width:326px;height:58px}
  .value__icon{position:absolute;top:6px;width:40px;height:40px;border-radius:8px;background:var(--brand-blue)}
  .value__icon svg{width:40px;height:40px}
  .value__text{position:absolute;top:4px;width:260px;font-size:10.5px;line-height:13px;color:var(--grey-dark)}
  .value__text b{color:var(--ink);font-weight:700}
  .value__rule{position:absolute;bottom:0;width:140px;height:2px;background:var(--brand-blue)}
  .value--left .value__icon{left:0}
  .value--left .value__text{left:52px}
  .value--left .value__rule{left:52px}
  .value--right .value__icon{right:0}
  .value--right .value__text{right:52px;text-align:right}
  .value--right .value__rule{right:52px}
  .page-mark{position:absolute;bottom:18px;left:0;right:0;text-align:center;font-size:9px;font-weight:700;color:var(--brand-blue)}

  /* welcome page */
  .welcome-name{position:absolute;left:26px;top:52px;font-size:16px;font-weight:700;color:var(--ink)}
  .welcome-stripes{left:206px;top:18px}
  .welcome-band{left:232px;top:18px;right:0;padding-left:14px}
  .intro{position:absolute;left:150px;top:84px;width:205px;font-size:10px;line-height:13px;font-style:italic;color:var(--grey-dark)}
  .photo{position:absolute;border-radius:10px}
  .team-photo{left:150px;top:140px;width:205px;height:150px;border-radius:0;
    background:linear-gradient(135deg,#eeeae4 0%,#d9cfc2 40%,#7fa5d4 70%,#5b86bb 100%)}
  .signatory{position:absolute;font-size:9px;line-height:11px;color:var(--grey-dark)}
  .signatory b{display:block;color:var(--ink);font-size:10px}
  .signatory::before{content:"";display:block;width:70px;height:1px;background:var(--ink);margin-bottom:4px}
  .signatory--owen{left:150px;top:306px}
  .signatory--derek{left:270px;top:306px}
  .sectors{position:absolute;left:150px;top:350px;width:205px;font-size:10px;line-height:13px;color:var(--grey-dark)}
  .tile{position:absolute}
  .tile--dark{left:30px;top:130px;width:68px;height:72px;border-radius:10px;background:var(--grey-dark)}
  .tile--blue{left:38px;top:212px;width:92px;height:86px}
  .tile--grey{left:62px;top:306px;width:70px;height:74px;border-radius:10px;background:var(--grey-mid)}
  .tile--black{left:306px;top:440px;width:48px;height:48px;border-radius:8px;background:#1b1b1b}

  /* cover */
  .brand-name{position:absolute;right:18px;top:40px;font-size:21px;font-weight:700;color:var(--ink)}
  .brand-band{position:absolute;left:200px;right:0;top:80px;height:7px;background:var(--brand-blue)}
  .photo--framed{border:4px solid var(--paper);border-radius:8px}
  .hero{left:0;top:190px;width:370px;height:223px;border-radius:0;
    background:radial-gradient(circle at 55% 45%,#3b5c8c 0,#2a3f63 18%,#7f8b96 34%,#9ba3ab 60%,#6f767d 100%)}
  .handshake{left:10px;top:100px;width:200px;height:108px;
    background:linear-gradient(135deg,#3a4454 0%,#c9cdd3 45%,#eef0f2 75%,#b8bcc2 100%)}
  .towers{left:208px;top:110px;width:88px;height:103px;
    background:linear-gradient(160deg,#8fb3dc 0%,#4b6d94 45%,#2d3f57 100%)}
  .typing{left:91px;top:404px;width:84px;height:88px;
    background:linear-gradient(150deg,#e6c7b2 0%,#b99884 40%,#3c3c3e 75%,#222 100%)}
  .crowd{left:175px;top:404px;width:183px;height:97px;
    background:linear-gradient(120deg,#c8c8c8 0%,#7c7370 35%,#4c5463 60%,#9a8f88 100%)}
  .shape{position:absolute}
  .shape--grey{left:296px;top:117px;width:69px;height:133px}
  .shape--blue{left:11px;top:332px;width:82px;height:162px}
  .tagline{position:absolute;left:110px;top:368px;width:250px;height:26px;background:var(--grey-dark);
    border-radius:6px;color:#fff;font-size:15px;line-height:26px;padding-left:12px}
  .tagline strong{font-weight:700}
</style>
</head>
<body>

  <section class="page page--values">
    <div class="section-band values-band">OUR VALUES</div>
    <div class="stripes values-stripes"><span></span><span></span><span></span><span></span></div>

    <div class="value value--left" style="top:86px">
      <div class="value__icon"><svg viewBox="0 0 40 40"><path d="M20 9 L30 13 V21 Q30 28 20 32 Q10 28 10 21 V13 Z" fill="none" stroke="#fff" stroke-width="2"/><path d="M15 20 L19 24 L26 16" fill="none" stroke="#fff" stroke-width="2.4"/></svg></div>
      <p class="value__text">Be <b>TRUSTED</b> by our team and clients, so that our opinions are sought and our recommendations valued.</p>
      <div class="value__rule"></div>
    </div>

    <div class="value value--right" style="top:150px">
      <div class="value__icon"><svg viewBox="0 0 40 40" fill="#fff"><circle cx="14" cy="18" r="4"/><circle cx="26" cy="18" r="4"/><circle cx="20" cy="13" r="4"/><path d="M8 31 Q14 22 20 31 Z M20 31 Q26 22 32 31 Z"/></svg></div>
      <p class="value__text">Have a tight knit relationship with our clients, so we are seen as a <b>PARTNER</b> and not just supplier.</p>
      <div class="value__rule"></div>
    </div>

    <div class="value value--left" style="top:214px">
      <div class="value__icon"><svg viewBox="0 0 40 40" fill="#fff"><rect x="10" y="22" width="4" height="9"/><rect x="16" y="18" width="4" height="13"/><rect x="22" y="14" width="4" height="17"/><path d="M9 17 L29 9" stroke="#fff" stroke-width="2"/></svg></div>
      <p class="value__text">Be focused on return-on-investment, but predominantly, always deliver <b>GREAT VALUE.</b></p>
      <div class="value__rule"></div>
    </div>

    <div class="value value--right" style="top:278px">
      <div class="value__icon"><svg viewBox="0 0 40 40"><rect x="9" y="9" width="22" height="15" fill="none" stroke="#fff" stroke-width="2"/><path d="M12 20 L17 15 L21 18 L27 12 M20 24 V28 M16 32 L20 28 L24 32" fill="none" stroke="#fff" stroke-width="2"/></svg></div>
      <p class="value__text"><b>DEVELOP &amp; INVEST IN</b> our own people to continually stay one step ahead.</p>
      <div class="value__rule"></div>
    </div>

    <div class="value value--left" style="top:342px">
      <div class="value__icon"><svg viewBox="0 0 40 40" fill="none" stroke="#fff" stroke-width="2"><circle cx="20" cy="20" r="11"/><ellipse cx="20" cy="20" rx="5" ry="11"/><path d="M9 20 H31"/></svg></div>
      <p class="value__text">Work relentlessly to deliver results for our clients, but ensure we collectively <b>ENJOY THE JOURNEY.</b></p>
      <div class="value__rule"></div>
    </div>

    <div class="value value--right" style="top:406px">
      <div class="value__icon"><svg viewBox="0 0 40 40" fill="none" stroke="#fff" stroke-width="2.2"><path d="M29 16 A10 10 0 0 0 11 16 M11 24 A10 10 0 0 0 29 24"/><path d="M26 12 L29 16 L33 13 M14 28 L11 24 L7 27"/></svg></div>
      <p class="value__text">Take <b>SOCIAL RESPONSIBILITY</b> seriously by supporting other worthwhile organisations.</p>
      <div class="value__rule"></div>
    </div>

    <div class="page-mark">tva</div>
  </section>

  <section class="page page--welcome">
    <div class="stripes welcome-stripes"><span></span><span></span><span></span><span></span></div>
    <div class="section-band welcome-band">OUR PEOPLE</div>
    <div class="welcome-name">Tolland Verge Advisory</div>

    <p class="intro">At TVA we constantly strive to deliver the best possible value for our clients. Importantly we recognize, it's our clients that define value, not us.</p>
    <div class="photo team-photo" role="img" aria-label="Photo of the two partners seated at a meeting table"></div>

    <div class="signatory signatory--owen"><b>Owen Marsh</b>Partner</div>
    <div class="signatory signatory--derek"><b>Derek Hallam</b>Partner</div>

    <p class="sectors">Our clients range from Norland Motors and our local manufacturers to healthcare organisations who run their own teams.</p>

    <div class="tile tile--dark"></div>
    <svg class="tile tile--blue" viewBox="0 0 92 86" aria-hidden="true"><path d="M10 4 H62 L88 43 L62 82 H10 Q4 82 4 76 V10 Q4 4 10 4 Z" fill="#376092"/></svg>
    <div class="tile tile--grey"></div>
    <div class="tile tile--black"></div>
    <div class="page-mark">tva</div>
  </section>

  <main class="page page--cover">
    <div class="brand-name">Tolland Verge Advisory</div>
    <div class="brand-band"></div>

    <div class="photo hero" role="img" aria-label="Light bulb containing the globe lying on a grey concrete surface"></div>
    <div class="photo photo--framed handshake" role="img" aria-label="Business handshake over a desk with laptop and papers"></div>
    <div class="photo photo--framed towers" role="img" aria-label="Glass office towers against a blue sky"></div>

    <svg class="shape shape--grey" viewBox="0 0 69 133" aria-hidden="true">
      <path d="M10 4 H59 Q65 4 65 10 V93 L34.5 129 L4 93 V10 Q4 4 10 4 Z" fill="#7d7e82" stroke="#fff" stroke-width="4" stroke-linejoin="round"/>
    </svg>
    <svg class="shape shape--blue" viewBox="0 0 82 162" aria-hidden="true">
      <path d="M4 48 L41 4 L72 29 Q78 34 78 41 V152 Q78 158 72 158 H10 Q4 158 4 152 Z" fill="#376092" stroke="#fff" stroke-width="4" stroke-linejoin="round"/>
    </svg>

    <div class="tagline">helping businesses <strong>evolve</strong></div>

    <div class="photo photo--framed typing" role="img" aria-label="Hands typing on a laptop keyboard"></div>
    <div class="photo photo--framed crowd" role="img" aria-label="Busy crowd of commuters in motion blur"></div>
  </main>

</body>
</html>
```